IRON SASH VIGOUR CERTIFICATE

Corvane Kickfist Inc is wanting to introduce a fitness system based upon certificates reflecting rank; White - Yellow - Blue - Red - Black.

The Certificate "MUST" have on it "IRON SASH VIGOUR"

The Certificate "MUST" have a martial arts theme!

The Certificate "MUST" reflect the fitness requirements for each rank.

The colour scheme for each Certificate "MUST" reflect the belt rank

The Certificate must include at least one martial arts graphic / motif

The certificate must have the Corvane KKF LOGO

We will need a certificate template that can be for all levels but reflect the rank and fitness level. The certificate can be either traditional or modern style but must reflect a martial art themes. The certificate must have the Corvane Kickfist logo incorporated into the certificate with signature space for senior instructors Gus Pelham & Nessa Crail-Pelham. The certificates should be eye catching and exciting to look at. It should bold and incorporate martial art motifs etc The fitness requirements are not onerous and the certificate system is created to incentivise physical activity and correct technique rather than creating an impossible standards only Olympians can achieve. The majority of our students are upper primary and lower secondary from 11yr-15yrs. Certificate should be youthful but not silly. The certificate template will be reproduced for each colour belt.White = 10 push ups 10 Sit ups 10 squats 10 Jumping Jacks 20 sec plank 400m continuous run Demonstrate beginner stretching techniqueYellow = 20 push ups 20 sit ups 20 squats 20 Jumping Jacks 40 Sec plank 800m continuous run Demonstrate intermediate stretching techniqueBlue = 30 push ups 30 sit ups 30 squats 30 Jumping Jacks 60 Sec plank 1200m continuous run Demonstrate intermediate stretching techniqueRed = 40 push ups 40 sit ups 40 squats 40 Jumping Jacks 75sec plank 1600m run Demonstrate advanced stretching techniqueBlack = 50 push ups 50 sit ups 50 squats 50 Jumping jacks 90 sec planks 2000m continuous run Demonstrate advanced stretching technique
Updates

HI Designers, Please go for modern and professionals. Several designs have used traditional motifs of water dragons or lattice bordering. This looks old school. Please do not use martial art silhouettes as it looks amateur. Definately looking for upmarket high quality presentations.

Logo Text

IRON SASH VIGOUR

Font styles to use
Decorative

Colors

Designer to choose colors to be used in the design.

Requirements
Must have
• This will be a template foe all coloured ranks of fitness, Be bold, memorable, should be themed to martial arts etc

```html
<!DOCTYPE html>
<html lang="en">
<head>
<meta charset="utf-8">
<title>Iron Sash Vigour Certificate – Yellow Belt</title>
<link rel="stylesheet" href="https://fonts.googleapis.com/css2?family=Oswald:wght@300;400;600&family=Fira+Sans+Condensed:wght@300;600;700&display=swap">
<style>
  :root {
    --paper: #f3f3f3;
    --navy: #394358;
    --frame-dark: #22283a;
    --belt-red: #e41c23;
    --rank-yellow: #ffff00;
    --figure-yellow: #f7f73e;
    --figure-shade: #e2dc2a;
    --badge-grey: #7b7b7b;
    --heading: #3a4459;
    --subheading: #555555;
    --title-ink: #1c1c1c;
    --sign-name: #252b3a;
    --white: #ffffff;
    --rule: #d9d9d9;
  }
  html, body {
    margin: 0;
    padding: 0;
    width: 1200px;
    height: 927px;
    overflow: hidden;
    background: var(--navy);
  }
  .certificate {
    display: block;
    width: 1200px;
    height: 927px;
  }
  .bg-paper { fill: var(--paper); }
  .bg-red { fill: var(--belt-red); }
  .bg-navy { fill: var(--navy); }
  .frame-dark { fill: none; stroke: var(--frame-dark); stroke-width: 15; }
  .frame-rank { fill: none; stroke: var(--rank-yellow); stroke-width: 15; stroke-linecap: square; }
  .title-main {
    font-family: "Oswald", sans-serif;
    font-weight: 600;
    font-size: 168px;
    fill: var(--heading);
  }
  .title-sub {
    font-family: "Oswald", sans-serif;
    font-weight: 300;
    font-size: 48px;
    fill: var(--subheading);
  }
  .title-rule { stroke: var(--subheading); stroke-width: 1; }
  .title-program {
    font-family: "Oswald", sans-serif;
    font-weight: 400;
    font-size: 90px;
    fill: var(--title-ink);
  }
  .club-mark { fill: var(--frame-dark); }
  .club-name {
    font-family: "Fira Sans Condensed", sans-serif;
    font-weight: 600;
    font-size: 15px;
    fill: var(--white);
    text-anchor: middle;
    letter-spacing: 1px;
  }
  .badge-ring { fill: var(--badge-grey); stroke: var(--rank-yellow); stroke-width: 5; }
  .badge-value {
    font-family: "Fira Sans Condensed", sans-serif;
    font-weight: 300;
    font-size: 34px;
    fill: var(--white);
    text-anchor: middle;
    letter-spacing: 2px;
  }
  .badge-unit {
    font-family: "Fira Sans Condensed", sans-serif;
    font-weight: 300;
    font-size: 17px;
    fill: var(--white);
    text-anchor: middle;
    letter-spacing: 2px;
  }
  .exercise-label {
    font-family: "Fira Sans Condensed", sans-serif;
    font-weight: 700;
    font-size: 22px;
    fill: var(--rank-yellow);
    text-anchor: middle;
    letter-spacing: 3px;
  }
  .skill-box { fill: none; stroke: var(--rank-yellow); stroke-width: 3; }
  .skill-text {
    font-family: "Fira Sans Condensed", sans-serif;
    font-weight: 700;
    font-size: 21px;
    fill: var(--rank-yellow);
    text-anchor: middle;
    letter-spacing: 3px;
  }
  .sign-line { stroke: var(--rule); stroke-width: 1; }
  .sign-name {
    font-family: "Oswald", sans-serif;
    font-weight: 600;
    font-size: 25px;
    fill: var(--sign-name);
    text-anchor: middle;
  }
  .sign-role {
    font-family: "Oswald", sans-serif;
    font-weight: 300;
    font-size: 23px;
    fill: var(--white);
    text-anchor: middle;
  }
</style>
</head>
<body>
<svg class="certificate" viewBox="0 0 1200 927" xmlns="http://www.w3.org/2000/svg">
  <defs>
    <linearGradient id="figure-tone" x1="0" y1="0" x2="1" y2="1">
      <stop offset="0" stop-color="var(--figure-yellow)"/>
      <stop offset="1" stop-color="var(--figure-shade)"/>
    </linearGradient>
  </defs>

  <!-- background bands -->
  <rect class="bg-paper" x="0" y="0" width="1200" height="927"/>
  <polygon class="bg-red" points="0,55 1200,508 1200,927 0,927"/>
  <polygon class="bg-navy" points="0,210 1200,596 1200,927 0,927"/>

  <!-- frame -->
  <rect class="frame-dark" x="26.5" y="28.5" width="1143" height="868"/>
  <polyline class="frame-rank" points="26.5,304 26.5,896.5 1169.5,896.5 1169.5,705"/>

  <!-- heading -->
  <text class="title-main" x="239" y="192" textLength="720" lengthAdjust="spacingAndGlyphs">CERTIFICATE</text>
  <line class="title-rule" x1="190" y1="240" x2="378" y2="240"/>
  <text class="title-sub" x="404" y="260" textLength="398" lengthAdjust="spacing">OF FITNESS LEVEL</text>
  <line class="title-rule" x1="818" y1="240" x2="1004" y2="240"/>
  <text class="title-program" x="327" y="352" textLength="508" lengthAdjust="spacingAndGlyphs">IRON SASH VIGOUR</text>

  <!-- club mark -->
  <g class="club-logo">
    <circle class="club-mark" cx="1071" cy="131" r="50"/>
    <text class="club-name" x="1071" y="127">CORVANE</text>
    <text class="club-name" x="1071" y="146">KKF</text>
  </g>

  <!-- student artwork area -->
  <rect x="44" y="383" width="492" height="496" rx="14" fill="url(#figure-tone)" opacity="0.9"
        role="img" aria-label="Illustration of two students in yellow uniforms performing a kick and a stance"/>

  <!-- fitness requirements -->
  <g class="requirement">
    <circle class="badge-ring" cx="613" cy="427" r="39"/>
    <text class="badge-value" x="613" y="432">20</text>
    <text class="badge-unit" x="613" y="449">sets</text>
    <text class="exercise-label" x="613" y="494">PUSH UPS</text>
  </g>
  <g class="requirement">
    <circle class="badge-ring" cx="779" cy="427" r="39"/>
    <text class="badge-value" x="779" y="432">20</text>
    <text class="badge-unit" x="779" y="449">sets</text>
    <text class="exercise-label" x="779" y="494">SQUATS</text>
  </g>
  <g class="requirement">
    <circle class="badge-ring" cx="946" cy="427" r="39"/>
    <text class="badge-value" x="946" y="432">20</text>
    <text class="badge-unit" x="946" y="449">sets</text>
    <text class="exercise-label" x="946" y="494">JUMPING JACKS</text>
  </g>
  <g class="requirement">
    <circle class="badge-ring" cx="613" cy="558" r="39"/>
    <text class="badge-value" x="613" y="563">20</text>
    <text class="badge-unit" x="613" y="580">sets</text>
    <text class="exercise-label" x="613" y="625">SIT UPS</text>
  </g>
  <g class="requirement">
    <circle class="badge-ring" cx="789" cy="558" r="39"/>
    <text class="badge-value" x="789" y="563">800</text>
    <text class="badge-unit" x="789" y="580">m</text>
    <text class="exercise-label" x="789" y="625">CONTINUOUS RUN</text>
  </g>
  <g class="requirement">
    <circle class="badge-ring" cx="965" cy="558" r="39"/>
    <text class="badge-value" x="965" y="563">40</text>
    <text class="badge-unit" x="965" y="580">sec</text>
    <text class="exercise-label" x="965" y="625">PLANK</text>
  </g>

  <!-- stretching skill -->
  <rect class="skill-box" x="619" y="662" width="332" height="87"/>
  <text class="skill-text" x="785" y="697">INTERMEDIATE</text>
  <text class="skill-text" x="785" y="724">STRETCHING TECHNIQUE</text>

  <!-- signatures -->
  <line class="sign-line" x1="572" y1="817" x2="808" y2="817"/>
  <text class="sign-name" x="690" y="851">NESSA CRAIL-PELHAM</text>
  <text class="sign-role" x="690" y="878">Senior Instructor</text>

  <line class="sign-line" x1="903" y1="817" x2="1139" y2="817"/>
  <text class="sign-name" x="1021" y="851">GUS PELHAM</text>
  <text class="sign-role" x="1021" y="878">Senior Instructor</text>
</svg>
</body>
</html>
```